Wine Label Design for the red wine named “Amber Moth Ridge” or “A/M”

Create an elegant yet simple (less is more) label for a red, full-bodied wine from a family-owned Herzegovinian vineyard by the river with 9 names. You can use elements such as the Calopteryx virgo, possibly the river shape, and ensure a coherent storytelling of the unique vineyard’s locality and meticulous, hand-picked grape cultivation.
Let’s craft a label that is not just seen, but is experienced and remembered.

Target Market(s)

Wine lovers that appreciate high quality wines

Industry/Entity Type

Wine, Family owned small producer

Requirements
Must have
• Name A/M, front and back label. Premium feel, uniqueness. Simple but interesting.
Nice to have
• Please see the images below as an idea of various directions. I am also leaning to embossed image on the label
Should not have
• Should not be overcrowded with text, too many images and objects

```html
<!DOCTYPE html>
<html lang="en">
<head>
<meta charset="utf-8">
<title>A/M Premium Wine Label</title>
<link rel="stylesheet" href="https://fonts.googleapis.com/css2?family=Playfair+Display:wght@400&family=Montserrat:wght@400&display=swap">
<style>
  :root {
    --wine-base: #a82a58;
    --wine-light: #b4305e;
    --wine-deep: #6a1c39;
    --wine-dark: #52030b;
    --ink-white: #ffffff;
  }
  html, body {
    margin: 0;
    padding: 0;
    width: 1200px;
    height: 2267px;
    overflow: hidden;
    background: var(--wine-base);
  }
  .label {
    position: relative;
    width: 1200px;
    height: 2267px;
    overflow: hidden;
    background: var(--wine-base);
  }
  .backdrop {
    position: absolute;
    inset: 0;
    width: 1200px;
    height: 2267px;
  }
  .emblem-area {
    position: absolute;
    left: 141px;
    top: 1154px;
    width: 790px;
    height: 736px;
    background: radial-gradient(closest-side at 50% 50%, rgba(82,3,11,0.95) 0%, rgba(82,3,11,0.85) 45%, rgba(82,3,11,0.4) 75%, rgba(82,3,11,0) 100%);
  }
  .wordmark {
    position: absolute;
    left: 0;
    width: 100%;
    top: 570px;
    margin: 0;
    text-align: center;
    font-family: "Playfair Display", serif;
    font-weight: 400;
    font-size: 172px;
    line-height: 1;
    letter-spacing: 0.3em;
    padding-left: 0.3em;
    box-sizing: border-box;
    color: var(--ink-white);
  }
  .grade {
    position: absolute;
    left: 0;
    width: 100%;
    top: 1996px;
    margin: 0;
    text-align: center;
    font-family: "Montserrat", sans-serif;
    font-weight: 400;
    font-size: 44px;
    line-height: 1.2;
    letter-spacing: 0.32em;
    padding-left: 0.32em;
    box-sizing: border-box;
    color: var(--ink-white);
  }
  .category {
    position: absolute;
    left: 0;
    width: 100%;
    top: 2138px;
    margin: 0;
    text-align: center;
    font-family: "Playfair Display", serif;
    font-weight: 400;
    font-size: 49px;
    line-height: 1.2;
    letter-spacing: 0.9em;
    padding-left: 0.9em;
    box-sizing: border-box;
    color: var(--ink-white);
  }
</style>
</head>
<body>
  <main class="label">
    <svg class="backdrop" viewBox="0 0 1200 2267" aria-hidden="true">
      <rect class="field" width="1200" height="2267" fill="var(--wine-base)"/>
      <path class="corner-glow" d="M0 0 H140 Q60 40 0 100 Z" fill="var(--wine-light)"/>
      <ellipse class="halo" cx="591" cy="825" rx="591" ry="762" fill="var(--wine-light)"/>
      <path class="lower-shade" d="M0 1414 Q230 1610 500 1625 Q880 1640 1163 1405 Q960 2000 696 2267 H0 Z" fill="var(--wine-deep)"/>
      <path class="corner-sweep" d="M1200 1947 Q1080 2150 960 2267 H1200 Z" fill="var(--wine-light)"/>
    </svg>

    <div class="emblem-area" role="img" aria-label="Silhouette of a banded demoiselle damselfly in flight"></div>

    <h1 class="wordmark">A/M</h1>
    <p class="grade">PREMIUM</p>
    <p class="category">WINE</p>
  </main>
</body>
</html>
```